Simple+Professional tech feel + warm and friendly box design for pet test kit

Project Name: 10-Minute Canine & Feline Rapid Test Kit Packaging Design
Target Brand Reference: VELUMAR (South Korea) styles
Design Style Direction: Professional tech feel + warm and friendly
Professionalism (Professional): Clear typography and distinct information hierarchy to reflect the product’s scientific rigor and accuracy.
Technological: Reflected through clean graphics and a minimalist layout.
Friendly: Utilise soft, warm colour combinations to convey care for pets and well-wishes for their health.
International: The design should align with mainstream aesthetics and avoid cultural ambiguities.

Target Market(s)
European Union and the United States
Industry/Entity Type
Veterinary Medical
Look and feel
Each slider illustrates characteristics of the customer's brand and the style your logo design should communicate.

```html
<!DOCTYPE html>
<html lang="en">
<head>
<meta charset="utf-8">
<title>ClarioPet 10-Minute Canine &amp; Feline Rapid Test Kit – Carton Dieline</title>
<link rel="stylesheet" href="https://fonts.googleapis.com/css2?family=Poppins:wght@300;400;600;700;800&family=Josefin+Sans:wght@300&display=swap">
<style>
  :root {
    --teal: #13a89e;
    --teal-soft: #bfe6e2;
    --teal-lid-soft: #55c2ba;
    --blue: #1761a8;
    --paper: #f5f6fa;
    --ink: #1b1b1b;
    --fold: #e0262b;
    --white: #ffffff;
  }
  html, body {
    margin: 0;
    padding: 0;
    width: 1200px;
    height: 682px;
    overflow: hidden;
    background: var(--white);
  }
  .carton {
    display: block;
    width: 1200px;
    height: 682px;
  }
  .die { fill: var(--paper); stroke: var(--ink); stroke-width: 2; }
  .fold { stroke: var(--fold); stroke-width: 1.6; fill: none; }
  .band-blue { fill: var(--blue); }
  .band-teal { fill: var(--teal); }
  .art-soft { fill: var(--teal-soft); }
  .art-lid { fill: var(--teal-lid-soft); }
  .sans { font-family: "Poppins", sans-serif; }
  .brand-bar { font-family: "Poppins", sans-serif; font-weight: 600; font-size: 32px; fill: var(--white); }
  .count-inline { font-family: "Poppins", sans-serif; font-weight: 700; font-size: 38px; fill: var(--teal); }
  .count-big { font-family: "Poppins", sans-serif; font-weight: 800; font-size: 118px; fill: var(--teal); }
  .count-label { font-family: "Poppins", sans-serif; font-weight: 400; font-size: 26px; fill: var(--teal); }
  .headline { font-family: "Poppins", sans-serif; font-weight: 700; font-size: 56px; fill: var(--blue); }
  .subhead { font-family: "Poppins", sans-serif; font-weight: 300; font-size: 56px; fill: var(--teal); }
  .species { font-family: "Josefin Sans", sans-serif; font-weight: 300; font-size: 50px; fill: var(--teal); }
  .maker { font-family: "Poppins", sans-serif; font-weight: 400; font-size: 27px; fill: var(--white); }
  .info { font-family: "Poppins", sans-serif; font-weight: 400; font-size: 21px; fill: var(--ink); }
  .info-strong { font-weight: 600; }
  .note { font-family: "Poppins", sans-serif; font-weight: 400; font-size: 15px; fill: var(--ink); }
  .ivd { font-family: "Poppins", sans-serif; font-weight: 700; font-size: 26px; fill: var(--ink); }
  .story { font-family: "Poppins", sans-serif; font-weight: 400; font-size: 21px; fill: var(--ink); }
  .lid-brand { font-family: "Poppins", sans-serif; font-weight: 600; font-size: 104px; fill: var(--white); }
</style>
</head>
<body>
<svg class="carton" viewBox="0 0 2363 1340" preserveAspectRatio="none" xmlns="http://www.w3.org/2000/svg">

  <!-- Dieline outer shapes -->
  <g class="dieline">
    <path class="die" d="M0,1338 L0,60 Q0,0 60,0 L737,0 Q797,0 797,60 L797,1338 L698,1338 Q648,1338 648,1288 L648,1218 L148,1218 L148,1288 Q148,1338 98,1338 Z"/>
    <path class="die" d="M797,502 L810,490 L810,328 L1110,328 Q1160,328 1160,378 L1166,480 L1181,492 L1181,502 Z"/>
    <path class="die" d="M2363,502 L2350,490 L2350,328 L2053,328 Q2003,328 1998,378 L1993,480 L1978,492 L1978,502 Z"/>
    <path class="die" d="M797,1028 L990,1178 L990,1240 Q990,1292 1040,1292 L1181,1292 L1181,1028 Z"/>
    <path class="die" d="M1181,1028 L1330,1220 L1330,1288 Q1330,1338 1380,1338 L1780,1338 Q1830,1338 1830,1288 L1830,1220 L1978,1028 Z"/>
    <path class="die" d="M1978,1028 L1976,1292 L2120,1292 Q2170,1292 2170,1240 L2170,1178 L2363,1028 Z"/>
    <rect class="die" x="797" y="502" width="1566" height="526"/>
  </g>

  <!-- Lid panel -->
  <g class="lid">
    <rect class="band-teal" x="0" y="122" width="797" height="380"/>
    <rect class="art-lid" x="220" y="165" width="95" height="95" rx="20" role="img" aria-label="Line drawing of a dog and cat silhouette"/>
    <rect class="art-lid" x="490" y="165" width="95" height="95" rx="20" role="img" aria-label="Line drawing of a dog and cat silhouette"/>
    <text class="lid-brand" x="400" y="392" text-anchor="middle" transform="rotate(180 400 392)">ClarioPet™</text>
  </g>

  <!-- Blue header bands -->
  <rect class="band-blue" x="0" y="537" width="495" height="53"/>
  <rect class="band-blue" x="753" y="537" width="1028" height="53"/>
  <rect class="band-blue" x="1918" y="537" width="445" height="53"/>

  <!-- Teal footer band -->
  <rect class="band-teal" x="0" y="984" width="2363" height="44"/>

  <!-- Back panel -->
  <g class="panel-back">
    <text class="brand-bar" x="44" y="575">ClarioPet™</text>
    <text class="count-inline" x="520" y="578">5 Tests/Kit</text>
    <rect x="44" y="626" width="709" height="252" rx="34" fill="var(--white)" stroke="var(--ink)" stroke-width="2"/>
    <rect class="art-soft" x="42" y="888" width="92" height="96" rx="14" role="img" aria-label="Outline drawing of a sitting cat"/>
    <text class="species" x="160" y="960">For Dogs and Cats</text>
    <rect class="art-soft" x="672" y="888" width="96" height="96" rx="14" role="img" aria-label="Outline drawing of a sitting dog"/>
    <text class="maker" x="742" y="1016" text-anchor="end">Norvelle</text>
  </g>

  <!-- Side panel: maker info -->
  <g class="panel-side-info" text-anchor="middle">
    <text class="info" x="992" y="685">A Clear View into Pet Health</text>
    <text class="info" x="992" y="710">Made by Norvelle</text>
    <text class="info info-strong" x="992" y="735">Norvelle Biotech Limited</text>
    <text class="info" x="992" y="760">Web:www.norvelle-bio.com</text>
    <text class="info" x="992" y="785">E-mail:sales@norvelle-bio.com</text>
    <text class="note" x="992" y="864">(For accurate results, please read the</text>
    <text class="note" x="992" y="882">instructions carefully before use)</text>
    <rect class="art-soft" x="852" y="912" width="206" height="50" rx="6" role="img" aria-label="Storage and handling symbols: single use, keep dry, keep away from sunlight, store between 4°C and 30°C"/>
    <rect x="1064" y="913" width="73" height="48" fill="none" stroke="var(--ink)" stroke-width="2"/>
    <text class="ivd" x="1100" y="946">IVD</text>
  </g>

  <!-- Front panel -->
  <g class="panel-front">
    <text class="brand-bar" x="1238" y="575">ClarioPet™</text>
    <text class="count-big" x="1854" y="606" text-anchor="middle">5</text>
    <text class="count-label" x="1856" y="641" text-anchor="middle">Tests/Kit</text>
    <text class="headline" x="1218" y="732" textLength="724" lengthAdjust="spacingAndGlyphs">10-Minute Canine &amp; Feline</text>
    <text class="subhead" x="1400" y="802">Rapid Test Kit</text>
    <rect x="1778" y="808" width="164" height="58" rx="10" fill="none" stroke="var(--blue)" stroke-width="4" transform="rotate(-15 1860 837)"/>
    <rect class="art-soft" x="1225" y="888" width="94" height="96" rx="14" role="img" aria-label="Outline drawing of a sitting dog"/>
    <text class="species" x="1345" y="960">For Dogs and Cats</text>
    <rect class="art-soft" x="1856" y="888" width="94" height="96" rx="14" role="img" aria-label="Outline drawing of a sitting cat"/>
    <text class="maker" x="1945" y="1013" text-anchor="end">Norvelle</text>
  </g>

  <!-- Side panel: brand story -->
  <g class="panel-side-story" text-anchor="middle">
    <text class="story" x="2170" y="622">ClarioPet is made by</text>
    <text class="story" x="2170" y="647">Norvelle, our name combines</text>
    <text class="story" x="2170" y="672">'Nor' for true direction with</text>
    <text class="story" x="2170" y="697">"velle" from</text>
    <text class="story" x="2170" y="722">Latin, representing both</text>
    <text class="story" x="2170" y="747">intelligent efficacy in our</text>
    <text class="story" x="2170" y="772">science and reverence for the</text>
    <text class="story" x="2170" y="797">spirit of life</text>
    <text class="story" x="2170" y="822">and the will to care in all</text>
    <text class="story" x="2170" y="847">creatures.</text>
  </g>

  <!-- Fold lines -->
  <g class="folds">
    <line class="fold" x1="0" y1="122" x2="797" y2="122"/>
    <line class="fold" x1="0" y1="502" x2="2363" y2="502"/>
    <line class="fold" x1="0" y1="1028" x2="2363" y2="1028"/>
    <line class="fold" x1="797" y1="502" x2="797" y2="1028"/>
    <line class="fold" x1="1181" y1="502" x2="1181" y2="1028"/>
    <line class="fold" x1="1978" y1="502" x2="1978" y2="1028"/>
  </g>
</svg>
</body>
</html>
```